BUSINESS CARD DESIGN

NAME- TODD MASVERIK
PHONE NUMER - 808- 451-7082
EMAIL- OFFICE@VORLINDE-GRADEWAY.COM
BACK OF CARD- SPEACIALIZES IN LAND CLEARING, FORESTRY MUCLHING AND EXCAVATION

Contact Information for Business Card

NAME- TODD MASVERIK PHONE NUMER - 808- 451-7082 EMAIL- OFFICE@VORLINDE-GRADEWAY.COM BACK OF CARD- SPEACIALIZES IN LAND CLEARING , MUCLHING AND EXCAVATION

```html
<!DOCTYPE html>
<html lang="en">
<head>
<meta charset="utf-8">
<title>Vorlinde Gradeway – Business Card</title>
<link rel="stylesheet" href="https://fonts.googleapis.com/css2?family=Orbitron:wght@900&family=Roboto:wght@400;500&display=swap">
<style>
  :root {
    --bg: #141416;
    --card: #262627;
    --card-deep: #1d1d1e;
    --pattern-a: #2a2a2b;
    --pattern-b: #4a4a4c;
    --gold: #fcc313;
    --amber: #f7a21b;
    --white: #f4f4f4;
    --ink: #1b1b1b;
  }
  * { box-sizing: border-box; margin: 0; padding: 0; }
  html, body { width: 1200px; height: 840px; overflow: hidden; background: var(--bg); }
  .canvas { position: relative; width: 1200px; height: 840px; }

  .card {
    position: absolute;
    width: 560px;
    height: 320px;
    border-radius: 22px;
    background: var(--card);
    border-bottom: 4px solid var(--amber);
    border-left: 2px solid var(--gold);
    overflow: hidden;
  }
  .card--back { left: 50px; top: 70px; background: var(--card-deep); }
  .card--front { left: 590px; top: 450px; }

  /* back side */
  .emblem-pattern {
    position: absolute; inset: 0;
    background: linear-gradient(110deg, var(--pattern-a) 0%, var(--pattern-a) 45%, var(--pattern-b) 100%);
  }
  .back-content {
    position: absolute; inset: 0;
    display: flex; flex-direction: column; align-items: center; justify-content: center;
    gap: 14px;
  }
  .brand { display: flex; align-items: center; gap: 12px; }
  .brand__dot { width: 34px; height: 34px; border-radius: 50%; background: var(--gold); }
  .brand__name {
    font-family: 'Orbitron', sans-serif; font-weight: 900;
    color: var(--gold); font-size: 24px; letter-spacing: 1px; line-height: 1.05;
  }
  .tag {
    background: var(--gold); color: var(--ink);
    font-family: 'Orbitron', sans-serif; font-weight: 900;
    font-size: 15px; padding: 4px 12px; letter-spacing: 1px;
  }
  .services {
    font-family: 'Roboto', sans-serif; font-weight: 400;
    color: var(--white); font-size: 14px; letter-spacing: 0.5px;
  }
  .services .bullet { color: var(--gold); margin: 0 6px; }

  /* front side */
  .front-brand { position: absolute; right: 36px; top: 40px; text-align: right; }
  .front-brand .brand__dot { width: 44px; height: 44px; margin-left: auto; margin-bottom: 10px; }
  .front-brand .brand__name { font-size: 22px; }
  .front-rule {
    position: absolute; left: 34px; right: 34px; top: 178px;
    height: 1px; background: var(--white);
  }
  .holder {
    position: absolute; left: 34px; top: 140px;
    font-family: 'Orbitron', sans-serif; font-weight: 900;
    color: var(--amber); font-size: 28px; letter-spacing: 1px;
  }
  .contacts {
    position: absolute; left: 34px; top: 200px;
    list-style: none; display: flex; flex-direction: column; gap: 10px;
    font-family: 'Roboto', sans-serif; color: var(--white); font-size: 19px;
  }
  .contacts li { display: flex; align-items: center; gap: 10px; }
  .contacts svg { width: 20px; height: 20px; fill: var(--amber); }
</style>
</head>
<body>
<div class="canvas">

  <section class="card card--back">
    <div class="emblem-pattern" role="img" aria-label="Repeating faint emblem pattern in dark grey tones"></div>
    <div class="back-content">
      <div class="brand">
        <span class="brand__dot"></span>
        <span class="brand__name">VORLINDE GRADEWAY<br>LLC HAWAII</span>
      </div>
      <div class="tag">SPEACIALIZES IN</div>
      <p class="services"><span class="bullet">●</span>LAND CLEARING<span class="bullet">●</span>MUCLHING<span class="bullet">●</span>EXCAVATION</p>
    </div>
  </section>

  <section class="card card--front">
    <div class="front-brand">
      <span class="brand__dot" style="display:block"></span>
      <span class="brand__name">VORLINDE GRADEWAY<br>LLC HAWAII</span>
    </div>
    <h1 class="holder">TODD MASVERIK</h1>
    <div class="front-rule"></div>
    <ul class="contacts">
      <li>
        <svg viewBox="0 0 24 24" aria-hidden="true"><path d="M6.6 10.8a15.1 15.1 0 0 0 6.6 6.6l2.2-2.2a1 1 0 0 1 1-.25 11.4 11.4 0 0 0 3.6.57 1 1 0 0 1 1 1V20a1 1 0 0 1-1 1A17 17 0 0 1 3 4a1 1 0 0 1 1-1h3.5a1 1 0 0 1 1 1c0 1.25.2 2.45.57 3.57a1 1 0 0 1-.25 1z"/></svg>
        808- 451-7082
      </li>
      <li>
        <svg viewBox="0 0 24 24" aria-hidden="true"><path d="M3 5h18a1 1 0 0 1 1 1v12a1 1 0 0 1-1 1H3a1 1 0 0 1-1-1V6a1 1 0 0 1 1-1zm1 2.2V17h16V7.2l-8 5.3z M4.8 7 12 11.8 19.2 7z"/></svg>
        office@vorlinde-gradeway.com
      </li>
    </ul>
  </section>

</div>
</body>
</html>
```